Drowned in paperwork book cover

Black book cover with image of man in a white coat with gold bars. Inspiration is the book cover below. The book is about medical corruption and how medical services are now all about the money. Full title:

Drowned in ‘Paperwork’
Why clerks and committees bury your plans under forms and how to break free regardless.

5.5 x 8 inches is the size of the book.

I"m trying to upload the image I liked; should be sort of like this

complete title: Drowned in ‘Paperwork’ Why clerks and committees bury your plans under forms and how to break free regardless. I attached a book cover that i liked. I'll try again. 5.5 inches by 8.5 inches cover size.

Target Market(s)

doctors and patients.

Colors

Designer to choose colors to be used in the design.

Requirements
Must have
• black cover

```html
<!DOCTYPE html>
<html lang="en">
<head>
<meta charset="utf-8">
<title>Drowned in ‘Paperwork’ – Book Cover</title>
<link rel="stylesheet" href="https://fonts.googleapis.com/css2?family=Creepster&family=Special+Elite&family=Alegreya:ital@1&family=Cormorant+Garamond:wght@500&display=swap">
<style>
  :root {
    --cover-black: #000000;
    --ink-white: #f4f4f4;
    --rule-grey: #8a8a8a;
    --title-red: #e0140c;
    --hex-fill-top: #1c1e20;
    --hex-fill-bottom: #4a4d50;
    --gold-light: #f7dd3b;
    --gold-dark: #c49a10;
    --coat-light: #e9edf0;
    --coat-shade: #9aa3aa;
  }
  html, body {
    margin: 0;
    padding: 0;
    overflow: hidden;
    background: var(--cover-black);
  }
  .cover {
    position: relative;
    width: 825px;
    height: 1200px;
    overflow: hidden;
    background: var(--cover-black);
  }
  .cover-art {
    position: absolute;
    inset: 0;
  }
  .title-main {
    position: absolute;
    left: 30px;
    top: 515px;
    width: 530px;
    margin: 0;
    text-align: center;
    font-family: "Creepster", "Impact", sans-serif;
    font-weight: 400;
    font-size: 92px;
    line-height: 1;
    letter-spacing: 6px;
    text-transform: uppercase;
    background: linear-gradient(to bottom, rgba(224,20,12,0) 0%, rgba(224,20,12,0) 30%, var(--title-red) 58%, var(--title-red) 100%);
    -webkit-background-clip: text;
    background-clip: text;
    color: transparent;
  }
  .title-joiner {
    position: absolute;
    left: 241px;
    top: 612px;
    width: 100px;
    text-align: center;
    font-family: "Cormorant Garamond", "Times New Roman", serif;
    font-weight: 500;
    font-size: 38px;
    line-height: 1;
    letter-spacing: 3px;
    color: var(--ink-white);
  }
  .title-subject {
    position: absolute;
    left: 40px;
    top: 676px;
    width: 510px;
    text-align: center;
    font-family: "Special Elite", "Courier New", monospace;
    font-size: 76px;
    line-height: 1;
    letter-spacing: 2px;
    color: var(--ink-white);
  }
  .title-rule {
    position: absolute;
    left: 9px;
    top: 769px;
    width: 613px;
    height: 1px;
    background: var(--rule-grey);
  }
  .subtitle {
    position: absolute;
    left: 60px;
    top: 795px;
    width: 500px;
    margin: 0;
    text-align: center;
    font-family: "Alegreya", "Georgia", serif;
    font-style: italic;
    font-size: 20px;
    line-height: 31px;
    color: var(--ink-white);
  }
  .author {
    position: absolute;
    left: 100px;
    top: 1138px;
    width: 420px;
    text-align: center;
    font-family: "Special Elite", "Courier New", monospace;
    font-size: 32px;
    line-height: 1;
    letter-spacing: 10px;
    color: var(--ink-white);
  }
</style>
</head>
<body>
<div class="cover">
  <svg class="cover-art" width="825" height="1200" viewBox="0 0 825 1200" xmlns="http://www.w3.org/2000/svg">
    <defs>
      <linearGradient id="hexFill" x1="0" y1="0" x2="1" y2="1">
        <stop offset="0" stop-color="#1c1e20"/>
        <stop offset="1" stop-color="#4a4d50"/>
      </linearGradient>
      <linearGradient id="goldFill" x1="0" y1="0" x2="0" y2="1">
        <stop offset="0" stop-color="#f7dd3b"/>
        <stop offset="1" stop-color="#c49a10"/>
      </linearGradient>
      <linearGradient id="coatFill" x1="0" y1="0" x2="0" y2="1">
        <stop offset="0" stop-color="#3a3f44"/>
        <stop offset="0.3" stop-color="#9aa3aa"/>
        <stop offset="1" stop-color="#e9edf0"/>
      </linearGradient>
    </defs>

    <g class="bg-hexes" fill="none" stroke="#1c1c1c" stroke-width="1.5">
      <polygon points="22,828 68,748 160,748 206,828 160,908 68,908"/>
    </g>

    <line class="connector-line" x1="0" y1="258" x2="385" y2="258" stroke="#f4f4f4" stroke-width="1.5"/>

    <polygon class="money-hex" points="385,258 468,116 633,116 716,258 633,400 468,400"
             fill="url(#hexFill)" stroke="#f4f4f4" stroke-width="3"/>
    <polyline class="money-hex-accent" points="413,250 478,138 577,138" fill="none" stroke="#f4f4f4" stroke-width="1.5"/>
    <rect class="coins-art" role="img" aria-label="Stacks of gold dollar coins"
          x="458" y="186" width="198" height="145" rx="18" fill="url(#goldFill)"/>

    <path class="doctor-photo" role="img" aria-label="Doctor in a white lab coat and blue glove raising his hand toward the coins"
          d="M518,445 L615,440 L738,378 L825,378 L825,1200 L625,1200 L622,900 L580,770 L575,570 L600,545 L560,535 L518,480 Z"
          fill="url(#coatFill)"/>
  </svg>

  <h1 class="title-main">Drowned</h1>
  <div class="title-joiner">IN</div>
  <div class="title-subject">PAPERWORK</div>
  <div class="title-rule"></div>
  <p class="subtitle">‘why clerks and committees bury your plans under forms and how to break free regardless.’</p>
  <div class="author">-AUTHOR NAME</div>
</div>
</body>
</html>
```